New business logo / Business Card Design

My company provides Interim Management and consultancy, for Facilities Services. Covers any aspect of facilities management, including M&E, helpdesk, asset management, supplier relationships, catering, cleaning etc. Company provides innovative solutions to exceed client needs, drawing on years of experience. Initial thoughts on logo are attached below. Fits with RAG status on projects, red, amber and green, with logo design colours around moving services from amber to green.

Target Market(s)

Facilities Management clients and service providers

Industry/Entity Type

Business

Contact Information for Business Card

Company Name = k7Rventures Ltd My name on card = Derek Haskins, Director Mobile = 07912365048 Email = Derek@k7rventuresltd.co.uk Twitter = @k7Rventures Ltd

Font styles to use
Sans Serif

Colors
f37122
00a990

Requirements
Must have
• Logo to be evident, with some background image in reference to Facilities Management

```html
<!DOCTYPE html>
<html lang="en">
<head>
<meta charset="utf-8">
<title>k7Rventures Ltd – Business Card</title>
<link rel="stylesheet" href="https://fonts.googleapis.com/css2?family=Montserrat:wght@400;600;800&display=swap">
<style>
  :root {
    --page-bg: #ecebe8;
    --card-white: #ffffff;
    --brand-orange: #ef6a25;
    --brand-green: #1e7a46;
    --ink-dark: #1f1f1f;
    --text-light: #ffffff;
    --divider: #ffffff;
  }
  * { box-sizing: border-box; margin: 0; padding: 0; }
  html, body {
    width: 1200px; height: 900px; overflow: hidden;
    background: var(--page-bg);
    font-family: "Montserrat", Arial, sans-serif;
  }
  .business-card {
    position: absolute; left: 150px; top: 193px;
    width: 900px; height: 514px;
    background: var(--card-white);
    box-shadow: 0 10px 30px rgba(0,0,0,0.18);
    overflow: hidden;
  }
  .brand-area {
    position: absolute; left: 0; top: 0; width: 100%; height: 300px;
    display: flex; align-items: center; justify-content: center; gap: 22px;
  }
  .brand-mark {
    width: 46px; height: 46px; border-radius: 50%;
    background: var(--brand-orange);
  }
  .brand-name {
    font-weight: 800; font-size: 64px; letter-spacing: -1px;
    color: var(--brand-green);
  }
  .contact-band {
    position: absolute; left: 0; top: 300px; width: 100%; height: 120px;
    background: var(--brand-orange);
    display: flex; align-items: center; justify-content: space-between;
    padding: 0 70px;
    color: var(--text-light);
  }
  .person-name {
    font-weight: 800; font-size: 26px; letter-spacing: 0.5px; text-transform: uppercase;
  }
  .person-title { font-weight: 400; font-size: 20px; margin-top: 4px; padding-left: 110px; }
  .contact-list { list-style: none; font-size: 18px; line-height: 30px; }
  .contact-list li { display: flex; align-items: center; gap: 12px; }
  .contact-icon { width: 16px; height: 16px; flex: none; }
  .band-divider {
    position: absolute; left: 0; top: 420px; width: 100%; height: 5px;
    background: var(--divider);
  }
  .services-band {
    position: absolute; left: 0; top: 425px; width: 100%; height: 89px;
    background: var(--brand-green);
    color: var(--text-light);
    display: flex; flex-direction: column; justify-content: center;
    padding-left: 70px;
    font-size: 20px; line-height: 28px;
  }
  .services-band .second-line { padding-left: 140px; }
</style>
</head>
<body>
  <section class="business-card">
    <div class="brand-area">
      <span class="brand-mark"></span>
      <span class="brand-name">k7Rventures Ltd</span>
    </div>

    <div class="contact-band">
      <div class="person">
        <p class="person-name">Derek Haskins</p>
        <p class="person-title">Director</p>
      </div>
      <ul class="contact-list">
        <li>
          <svg class="contact-icon" viewBox="0 0 16 16" aria-hidden="true">
            <path d="M3 1.5 L6 1.5 L7 5 L5.2 6.2 Q6.5 9.5 9.8 10.8 L11 9 L14.5 10 L14.5 13 Q14.5 14.5 13 14.5 Q2 13.5 1.5 3 Q1.5 1.5 3 1.5 Z" fill="#ffffff"/>
          </svg>
          07912365048
        </li>
        <li>
          <svg class="contact-icon" viewBox="0 0 16 16" aria-hidden="true">
            <rect x="1" y="3" width="14" height="10" fill="#ffffff"/>
            <path d="M1 3 L8 9 L15 3" fill="none" stroke="#ef6a25" stroke-width="1.4"/>
          </svg>
          Derek@k7rventuresltd.co.uk
        </li>
        <li>
          <svg class="contact-icon" viewBox="0 0 16 16" aria-hidden="true">
            <circle cx="8" cy="8" r="6" fill="#ffffff"/>
          </svg>
          @k7Rventures Ltd
        </li>
      </ul>
    </div>

    <div class="band-divider"></div>

    <div class="services-band">
      <p>helpdesk, asset management, supplier relationships</p>
      <p class="second-line">catering, cleaning etc</p>
    </div>
  </section>
</body>
</html>
```